mediation practice website build

Looking to create a website for new civil mediation practice. Pages would be "home", "about us", "about mediation", "scheduling" (perhaps with some kind of calendar function), "contact us". Would love to be able to update content/text myself.
Target Market(s)
Small to midsize businesses and attorneys representing those size businesses in pending disputes.
Industry/Entity Type
Build
Look and feel
Each slider illustrates characteristics of the customer's brand and the style your logo design should communicate.

```html
<!DOCTYPE html>
<html lang="en">
<head>
<meta charset="utf-8">
<title>Brookline Mediation</title>
<link href="https://fonts.googleapis.com/css2?family=Arimo:wght@400;700&family=Cousine:wght@400;700&display=swap" rel="stylesheet">
<style>
:root{
  --navy:#0e3f78;
  --tab:#3a6a9a;
  --tab-dark:#24507e;
  --band:#8aa98a;
  --panel:#c5d5c5;
  --ink:#123f6e;
  --login-green:#1c4f1c;
  --btn-green:#4f8a4f;
  --rule:#2d5f8a;
  --white:#ffffff;
}
*{margin:0;padding:0;box-sizing:border-box}
html,body{width:1144px;height:1200px;overflow:hidden;background:var(--white)}
body{position:relative;font-family:"Arimo",Arial,sans-serif;color:var(--ink)}
.brand{position:absolute;left:31px;top:102px;display:flex;align-items:center;gap:14px}
.brand-name{font-weight:700;font-size:44px;line-height:48px;color:var(--navy);letter-spacing:1px}
.brand-mark{width:22px;height:22px;border-radius:50%;background:var(--navy)}
.login{position:absolute;left:908px;top:101px;width:170px}
.login h2{font-size:17px;color:var(--login-green);margin-bottom:10px}
.login .field{display:block;width:152px;height:26px;background:var(--tab);color:var(--white);font-size:14px;padding:4px 9px;margin-bottom:11px;box-shadow:3px 3px 3px #777}
.login .btn{display:inline-block;width:54px;height:26px;background:linear-gradient(var(--btn-green),#2f6a2f);color:var(--white);font-size:11px;font-weight:700;text-align:center;line-height:26px;border:1px solid #bbb}
.nav{position:absolute;left:26px;top:224px;display:flex;gap:0}
.nav a{display:block;width:132px;height:33px;line-height:33px;text-align:center;color:var(--white);font-size:15px;text-decoration:none;background:var(--tab);clip-path:polygon(0 0,88% 0,100% 45%,100% 100%,0 100%)}
.nav a.active{background:var(--navy);font-weight:700;box-shadow:3px 3px 3px #555}
.tagline{position:absolute;left:26px;top:257px;width:1078px;height:56px;background:var(--band);font-weight:700;font-size:20px;color:var(--navy);padding:16px 0 0 51px}
.panel{position:absolute;top:320px;height:217px;background:var(--panel)}
.news-intro{left:26px;width:354px;padding:12px 16px}
.news-intro h2{font-size:28px;color:var(--navy);margin-bottom:28px}
.news-intro p{font-size:13.2px;line-height:14px;margin-bottom:14px}
.calendar-panel{left:388px;width:353px;padding:6px}
.calendar{position:absolute;left:6px;top:6px;width:187px;border:2px solid #333;background:#c8c8c8;font-family:"Cousine",monospace;font-size:11px}
.calendar .head{display:flex;justify-content:space-between;padding:3px 8px;font-weight:700;font-size:11px;color:#222}
.calendar table{width:100%;border-collapse:collapse;background:var(--white)}
.calendar th{background:#ddd;font-weight:400;border:1px solid #888;height:21px;font-size:11px}
.calendar td{border:1px solid #888;height:23px;text-align:center;color:#222}
.calendar td.today{background:#222;color:var(--white)}
.calendar .foot{text-align:center;font-weight:700;padding:4px 0;color:#222}
.calendar-panel .event{position:absolute;left:204px;top:20px;width:142px}
.event h3{font-size:16px;margin-bottom:10px;color:var(--navy)}
.event p{font-size:13.2px;line-height:14.3px}
.brand-panel{left:750px;width:354px;display:flex;align-items:center;justify-content:center}
.brand-panel span{font-weight:700;font-size:27px;color:var(--navy);letter-spacing:1px}
.feature{position:absolute;left:26px;top:545px;width:1078px;height:466px;background:linear-gradient(90deg,#8a9288 0%,#a6b6a6 55%,#9ab69a 100%)}
.feature-art{position:absolute;left:50px;top:110px;width:600px;height:240px;display:flex;align-items:center;justify-content:center;background:linear-gradient(90deg,rgba(255,255,255,0.05),rgba(255,255,255,0.12))}
.feature-art span{font-weight:700;font-size:54px;color:#2d5a72;letter-spacing:2px}
.latest{position:absolute;left:747px;top:30px;width:310px}
.latest h2{font-size:28px;color:var(--navy);display:inline-block;border-bottom:1px solid var(--navy);padding-bottom:4px;margin-bottom:18px}
.latest p{font-size:13.2px;line-height:14.3px}
.latest time{display:block;color:var(--white);font-size:13.2px;margin-bottom:16px}
.footer-rule{position:absolute;left:26px;top:1025px;width:1078px;border-top:1px solid var(--rule)}
.footer{position:absolute;right:40px;top:1040px;font-size:13.5px;font-weight:700;color:#123a4c}
</style>
</head>
<body>
<header>
  <div class="brand"><span class="brand-name">BROOKLINE<br>MEDIATION</span><span class="brand-mark"></span></div>
  <form class="login">
    <h2>Member Login</h2>
    <span class="field">User Name...........</span>
    <span class="field">Password............</span>
    <span class="btn">LOGIN</span>
  </form>
  <nav class="nav">
    <a class="active" href="#">Home</a>
    <a href="#">About Mediation</a>
    <a href="#">Scheduling</a>
    <a href="#">Our Company</a>
    <a href="#">Contact Us</a>
  </nav>
</header>
<div class="tagline">Looking to create a website for new civil mediation practice. "......................................................</div>

<section class="panel news-intro">
  <h2>What’s New</h2>
  <p>Looking to create a website for new civil mediation practice. Pages would be "home", "about us", "about mediation", "scheduling" (perhaps with some</p>
  <p>Looking to create a website for new civil mediation practice. Pages would be "home", "about us", "about mediation", "scheduling" (perhaps with some kind of calendar function), "contact us". Would love to be able to update content/text myself.</p>
</section>

<section class="panel calendar-panel">
  <div class="calendar">
    <div class="head"><span>« ‹</span><span>June 2011</span><span>› »</span></div>
    <table>
      <tr><th>S</th><th>M</th><th>T</th><th>W</th><th>T</th><th>F</th><th>S</th></tr>
      <tr><td></td><td></td><td></td><td>1</td><td>2</td><td>3</td><td>4</td></tr>
      <tr><td>5</td><td>6</td><td>7</td><td>8</td><td>9</td><td class="today">10</td><td>11</td></tr>
      <tr><td>12</td><td>13</td><td>14</td><td>15</td><td>16</td><td>17</td><td>18</td></tr>
      <tr><td>19</td><td>20</td><td>21</td><td>22</td><td>23</td><td>24</td><td>25</td></tr>
      <tr><td>26</td><td>27</td><td>28</td><td>29</td><td>30</td><td></td><td></td></tr>
      <tr><td></td><td></td><td></td><td></td><td></td><td></td><td></td></tr>
    </table>
    <div class="foot">[close] [clear]</div>
  </div>
  <div class="event">
    <h3>June 10, 2011</h3>
    <p>Looking to create a website for new civil mediation practice. Pages would be "home", "about us", "about mediation", "scheduling" (perhaps with some kind of calendar function), "contact us". Would</p>
  </div>
</section>

<section class="panel brand-panel"><span>BROOKLINE MEDIATION</span></section>

<section class="feature">
  <div class="feature-art" role="img" aria-label="Large soft-focus brand name banner"><span>BROOKLINE MEDIATION</span></div>
  <div class="latest">
    <h2>Lastest News</h2>
    <p>Looking to create a website for new civil mediation practice. Pages would be "home", "about us", "about mediation", "scheduling" (perhaps with some kind of calendar function), "contact us". Would love to be able to update content/text myself.</p>
    <time>08 May, 2011</time>
    <p>Looking to create a website for new civil mediation practice. Pages would be "home", "about us", "about mediation", "scheduling" (perhaps with some kind of calendar function), "contact us". Would love to be able to update content/text myself.</p>
    <time>06 May, 2011</time>
    <p>Looking to create a website for new civil mediation practice. Pages would be "home", "about us", "about mediation", "scheduling" (perhaps with some kind of calendar function), "contact us". Would love to be able to update content/text myself.</p>
    <time>02 May, 2011</time>
  </div>
</section>

<div class="footer-rule"></div>
<footer class="footer">© 2011 Brookline Mediation. All rights reserved.</footer>
</body>
</html>
```